Business Card Design

My company does Complete service and Maintenance for all off road toys ie: Atvs, golf carts, Dirtbikes and endures, Waverunners and Jetskis, etc... We are also taking special orders for customers and providing them with service and maintenance plans.
I want the card to appeal to young and old maybe some graphic stuff with atvs and golf carts too. We are going to offer pick up and drop off options too. Business cards and maybe brochure. Also doing Guided Waterfall Tours !
Target Market(s)
People that like to fun!
Industry/Entity Type
Business
Contact Information for Business Card
Trailblaze Garage , Daniel R Hollis ,Owner/ Technician
Danatthedunes@quillmail.net Golf Carts, Quads, Dirtbikes, and Off-Road Toys , Service and Maintenance. Ph# 507 6819 2275 Serving the Pacific Coast of Panama! Oil, Lube, and filter changes. Tuning and fine tuning, Complete details and custom orders. Order your new machine here with a complete service and Maintenance plan

```html
<!DOCTYPE html>
<html lang="en">
<head>
<meta charset="utf-8">
<title>Trailblaze Garage – Business Card</title>
<link rel="stylesheet" href="https://fonts.googleapis.com/css2?family=Titillium+Web:wght@400;600;700&display=swap">
<style>
  :root {
    --canvas: #e9e7e4;
    --card-dark: #12171d;
    --card-darker: #0a0d11;
    --blue-bright: #2aa7e2;
    --blue-deep: #1570c4;
    --blue-text: #3bb4ee;
    --purple: #4a3a9a;
    --navy-ink: #0c1a2e;
    --white: #f2f5f8;
    --muted: #c9d2db;
  }
  * { box-sizing: border-box; margin: 0; padding: 0; }
  html, body {
    width: 1200px; height: 800px; overflow: hidden;
    background: var(--canvas);
    font-family: "Titillium Web", "Segoe UI", sans-serif;
  }
  .stage {
    width: 1200px; height: 800px;
    display: flex; align-items: center; justify-content: center; gap: 40px;
  }
  .card {
    position: relative;
    width: 540px; height: 309px;
    overflow: hidden;
    border-radius: 3px;
    box-shadow: 0 10px 24px rgba(0,0,0,.22);
  }

  /* Back side */
  .card-back {
    background: linear-gradient(160deg, var(--card-dark), var(--card-darker));
    color: var(--white);
    display: flex; flex-direction: column; align-items: center;
    padding: 46px 28px 0;
    text-align: center;
  }
  .brand-name {
    font-weight: 700;
    text-transform: uppercase;
    letter-spacing: 3px;
    line-height: 1;
  }
  .card-back .brand-name {
    font-size: 44px;
    color: var(--blue-text);
    display: flex; align-items: center; gap: 14px;
  }
  .brand-mark {
    width: 16px; height: 16px; background: var(--blue-text);
  }
  .service-list {
    margin-top: 26px;
    font-size: 12px; font-weight: 600;
    letter-spacing: 1px;
    color: var(--blue-text);
    text-transform: uppercase;
  }
  .service-list .sep { color: var(--white); margin: 0 5px; }
  .service-details {
    margin-top: 30px;
    font-size: 13px; line-height: 1.65;
    color: var(--muted);
  }
  .service-details .sep { color: var(--blue-text); margin: 0 5px; }

  /* Front side */
  .card-front { background: var(--card-dark); color: var(--white); }
  .front-bands { position: absolute; inset: 0; }
  .card-front .brand-name {
    position: absolute; right: 34px; top: 26px;
    font-size: 40px;
    color: var(--navy-ink);
    text-align: right;
  }
  .card-front .brand-name span { display: block; }
  .card-front .brand-name span + span { margin-top: 6px; font-size: 34px; }
  .contact {
    position: absolute; left: 30px; top: 128px;
  }
  .contact-name {
    font-size: 21px; font-weight: 700;
    color: var(--blue-text);
    text-transform: uppercase; letter-spacing: 1px;
    line-height: 1.1;
  }
  .contact-role { font-size: 15px; color: var(--white); margin-bottom: 12px; }
  .contact-line {
    display: flex; align-items: center; gap: 9px;
    font-size: 15px; line-height: 1.55;
  }
  .contact-line svg { width: 13px; height: 13px; flex: none; }
  .photo {
    position: absolute;
    width: 64px; height: 64px;
    border: 4px solid var(--blue-deep);
  }
  .photo-quad { left: 378px; top: 146px; background: linear-gradient(135deg, #eef1f4, #8fa6c4); }
  .photo-jump { left: 378px; top: 218px; background: linear-gradient(135deg, #8a7a5c, #2f5fa8); }
  .photo-rider { left: 450px; top: 218px; background: linear-gradient(135deg, #5a4a34, #2a4f93); }
</style>
</head>
<body>
<main class="stage">

  <section class="card card-back" aria-label="Business card back">
    <h1 class="brand-name"><span class="brand-mark"></span>Trailblaze Garage</h1>
    <p class="service-list">
      Carts<span class="sep">|</span>Quads<span class="sep">|</span>Dirtbikes<span class="sep">|</span>Off-Road Toys<span class="sep">|</span>Service<span class="sep">|</span>Maintenance
    </p>
    <p class="service-details">
      Serving the Pacific Coast of Panama<span class="sep">|</span>Oil Lube and filter changes<br>
      Tuning and fine tuning<span class="sep">|</span>Complete details and custom orders<br>
      Purchase a New or Used machine here with complete service and Maintenance plan
    </p>
  </section>

  <section class="card card-front" aria-label="Business card front">
    <svg class="front-bands" viewBox="0 0 540 309" preserveAspectRatio="none" aria-hidden="true">
      <defs>
        <linearGradient id="blueBand" x1="0" y1="0" x2="1" y2="1">
          <stop offset="0" stop-color="#2fb0e8"/>
          <stop offset="1" stop-color="#1467bd"/>
        </linearGradient>
      </defs>
      <polygon points="0,0 540,0 540,262 0,78" fill="url(#blueBand)"/>
      <polygon points="0,78 540,262 540,276 0,92" fill="#4a3a9a"/>
    </svg>

    <h2 class="brand-name"><span>Trailblaze</span><span>Garage</span></h2>

    <div class="contact">
      <p class="contact-name">Daniel R Hollis</p>
      <p class="contact-role">Owner/ Technician</p>
      <p class="contact-line">
        <svg viewBox="0 0 14 14" aria-hidden="true"><rect x="0" y="0" width="14" height="14" rx="2" fill="#3bb4ee"/><rect x="4.5" y="2.5" width="5" height="9" rx="1" fill="#12171d"/></svg>
        507 6819 2275
      </p>
      <p class="contact-line">
        <svg viewBox="0 0 14 14" aria-hidden="true"><rect x="0" y="0" width="14" height="14" rx="2" fill="#3bb4ee"/><path d="M3 4.5h8v5H3z M3 4.5l4 3 4-3" fill="none" stroke="#12171d" stroke-width="1.2"/></svg>
        Danatthedunes@quillmail.net
      </p>
    </div>

    <div class="photo photo-quad" role="img" aria-label="Photo of a blue sport quad"></div>
    <div class="photo photo-jump" role="img" aria-label="Photo of a rider jumping a quad in the dirt"></div>
    <div class="photo photo-rider" role="img" aria-label="Photo of a rider on a quad on a dirt trail"></div>
  </section>

</main>
</body>
</html>
```